Postcard new promo

Promotion of new equipment. on the backside promo for servicing equipment
Picture name:
File 1: TQX-350 Auto Refractor/Keratometer. put a price of 3995.00. 2 Years Warranty
File 7: TQX-450 Auto Refractor/Keratometer. Price of 4995.00. 2 Years Warranty.
File 2: TVB-600 Autolensometer. Price of 2295.00. 2 Years Warranty.
File 3: DRA 4400 Digital Slit Lamp with camera and software. Price 11,995,00. 2 Years Warranty.
File 8: MEV PRT-3LED Slit Lamp. Price 2895.00. 2 Years Warranty.
File 4: MEV Digital Acuity System 24". Price 850.00. 2 Years Warranty.
Above is all brand new equipment.

File 5: Please use on the Dalvoss Exam Lane. Refurbished Dalvoss Exam Lane. Price 8500.00. Free Delivery and Installation. 1 Year Warranty.

File 6: The Showroom picture please use with some ideas, its about my company.

on the backside please use File 9: Refractor Cleaning only 295.00.
Below please insert File 10.

Eye Doctors

Sans Serif

• My logo, web site and my telephone number.

```html
<!DOCTYPE html>
<html lang="en">
<head>
<meta charset="utf-8">
<title>Lakeside Optic Services – Postcard</title>
<link rel="stylesheet" href="https://fonts.googleapis.com/css2?family=Ubuntu:wght@400;500;700&family=Montserrat:wght@700;800&family=Oswald:wght@500;600&display=swap">
<style>
  :root{
    --stage:#616161;
    --navy:#233f8f;
    --royal:#2c56a8;
    --sky:#2fa3d8;
    --sky-light:#8fc7ea;
    --ice:#eef1f5;
    --ink:#1c1c1c;
    --muted:#555b63;
    --white:#ffffff;
  }
  *{box-sizing:border-box;margin:0;padding:0}
  html,body{width:1088px;height:1200px;overflow:hidden;background:var(--stage)}
  body{position:relative;font-family:"Ubuntu",sans-serif}
  .card{position:absolute;left:224px;width:641px;height:428px;overflow:hidden;box-shadow:6px 8px 10px rgba(0,0,0,.35)}
  .card--front{top:142px;background:linear-gradient(135deg,#ffffff 0%,var(--ice) 60%,#e4e8ee 100%)}
  .card--back{top:614px;background:var(--white)}
  .layer{position:absolute;left:0;top:0;width:641px;height:428px}
  .abs{position:absolute}

  .brand{position:absolute;display:flex;align-items:center;gap:8px;color:var(--navy);font-family:"Ubuntu",sans-serif;font-weight:400;letter-spacing:2px;line-height:1.15}
  .brand__dot{width:22px;height:22px;border-radius:50%;background:var(--sky);flex:none}
  .brand--front{left:372px;top:40px;font-size:21px}
  .brand--back{left:326px;top:28px;font-size:12px;gap:5px}
  .brand--back .brand__dot{width:13px;height:13px}

  .headline{position:absolute;left:17px;top:152px;font-family:"Montserrat",sans-serif;font-weight:800;color:transparent;-webkit-text-stroke:1px var(--white);line-height:1}
  .headline__sm{display:block;font-size:27px;letter-spacing:.5px}
  .headline__big{display:block;font-size:52px;color:var(--white);-webkit-text-stroke:0;margin:3px 0 2px}
  .headline__md{display:block;font-size:19.5px;letter-spacing:.3px;margin-top:3px}

  .address{position:absolute;left:17px;top:371px;color:#5cb4ea;font-size:11px;line-height:14.5px}

  .sell-tab{position:absolute;left:447px;top:127px;width:194px;height:30px;color:var(--white);font-family:"Montserrat",sans-serif;font-weight:800;font-size:18px;line-height:30px;text-align:right;padding-right:25px;white-space:nowrap}
  .sell-list{position:absolute;right:17px;top:160px;list-style:none;text-align:right}
  .sell-list li{color:#eaf6fd;font-size:16px;font-weight:500;line-height:21.1px;display:flex;justify-content:flex-end;align-items:center;gap:7px}
  .chev{width:11px;height:11px;flex:none}

  .contact-front{position:absolute;right:17px;top:350px;list-style:none}
  .contact-front li{display:flex;justify-content:flex-end;align-items:center;gap:7px;font-size:16px;color:var(--ink);line-height:21.5px}
  .ico{width:17px;height:17px;flex:none}

  .also-title{position:absolute;left:17px;top:14px;font-family:"Montserrat",sans-serif;font-weight:800;font-size:17px;color:var(--navy)}
  .also-text{position:absolute;left:17px;top:40px;width:200px;font-size:9.5px;line-height:12.5px;color:var(--muted)}
  .services-title{position:absolute;left:17px;top:99px;font-family:"Montserrat",sans-serif;font-weight:800;font-size:18px;color:var(--white)}
  .services{position:absolute;left:19px;top:133px;list-style:none}
  .services li{position:relative;padding-left:20px;color:var(--white);font-size:15px;font-weight:500;line-height:21.8px}
  .services li::before{content:"";position:absolute;left:0;top:6px;width:11px;height:11px;border-radius:50%;background:var(--sky)}
  .promo-label{position:absolute;left:160px;top:276px;font-family:"Oswald",sans-serif;font-weight:600;font-size:11.5px;color:var(--royal);letter-spacing:.3px}
  .promo-price{position:absolute;left:160px;top:291px;font-family:"Oswald",sans-serif;font-weight:600;font-size:21px;color:var(--navy)}
  .contact-back{position:absolute;left:22px;top:362px;list-style:none}
  .contact-back li{display:flex;align-items:center;gap:10px;font-size:13.5px;color:var(--white);line-height:19.6px}
  .ico--sm{width:14px;height:14px}
</style>
</head>
<body>

<section class="card card--front" aria-label="Postcard front">
  <svg class="layer" viewBox="0 0 641 428" aria-hidden="true">
    <defs>
      <linearGradient id="blueFront" x1="0" y1="0" x2="0" y2="1">
        <stop offset="0" stop-color="#2c4f9e"/><stop offset="1" stop-color="#2a57b0"/>
      </linearGradient>
      <linearGradient id="band" x1="0" y1="0" x2="1" y2="0">
        <stop offset="0" stop-color="#2b9ad3"/><stop offset="1" stop-color="#35a9dd"/>
      </linearGradient>
      <linearGradient id="photo" x1="0" y1="0" x2="0" y2="1">
        <stop offset="0" stop-color="#ffffff"/><stop offset="1" stop-color="#d9dde3"/>
      </linearGradient>
    </defs>
    <polygon points="0,0 191,0 250,214 197,428 0,428" fill="url(#blueFront)"/>
    <polygon points="330,127 641,127 641,314 330,314" fill="url(#band)"/>
    <polygon points="447,127 641,127 641,157 462,157" fill="var(--navy)"/>
  </svg>

  <div class="brand brand--front"><span class="brand__dot"></span><span>LAKESIDE OPTIC<br>SERVICES</span></div>

  <h1 class="headline">
    <span class="headline__sm">SALE ON</span>
    <span class="headline__big">NEW</span>
    <span class="headline__md">OPHTHALMIC</span>
    <span class="headline__md">EQUIPMENT</span>
  </h1>

  <svg class="layer" viewBox="0 0 641 428">
    <g stroke="#ffffff" stroke-width="3">
      <polygon role="img" aria-label="Photo: TQX-350 auto refractor/keratometer" points="273,-5 328,50 273,105 218,50" fill="url(#photo)"/>
      <polygon role="img" aria-label="Photo: TQX-450 auto refractor/keratometer" points="212,48 267,103 212,158 157,103" fill="url(#photo)"/>
      <polygon role="img" aria-label="Photo: TVB-600 autolensometer" points="333,48 388,103 333,158 278,103" fill="url(#photo)"/>
      <polygon role="img" aria-label="Photo: refurbished Dalvoss exam lane with chair and stand" points="273,104 383,214 273,324 163,214" fill="url(#photo)"/>
      <polygon role="img" aria-label="Photo: DRA 4400 digital slit lamp" points="212,273 267,328 212,383 157,328" fill="url(#photo)"/>
      <polygon role="img" aria-label="Photo: MEV PRT-3LED slit lamp" points="333,273 388,328 333,383 278,328" fill="url(#photo)"/>
      <polygon role="img" aria-label="Photo: MEV digital acuity system 24 inch" points="273,326 328,381 273,436 218,381" fill="url(#photo)"/>
    </g>
    <g fill="#2a8fd0">
      <polygon points="240,72 306,72 273,105"/>
      <polygon points="179,125 245,125 212,158"/>
      <polygon points="300,125 366,125 333,158"/>
      <polygon points="223,274 323,274 273,324"/>
      <polygon points="179,350 245,350 212,383"/>
      <polygon points="300,350 366,350 333,383"/>
      <polygon points="240,403 306,403 273,436"/>
    </g>
    <g fill="var(--navy)" stroke="#ffffff" stroke-width="1">
      <circle cx="298" cy="64" r="5"/><circle cx="237" cy="117" r="5"/><circle cx="358" cy="117" r="5"/>
      <circle cx="318" cy="262" r="6"/><circle cx="237" cy="342" r="5"/><circle cx="358" cy="342" r="5"/><circle cx="298" cy="395" r="5"/>
    </g>
    <g font-family="Oswald, sans-serif" font-weight="600" fill="#ffffff" text-anchor="middle">
      <text x="273" y="81" font-size="8">3995.00</text>
      <text x="212" y="134" font-size="8">4995.00</text>
      <text x="333" y="134" font-size="8">2295.00</text>
      <text x="273" y="284" font-size="8.5">8500.00</text>
      <text x="212" y="359" font-size="8">11,995.00</text>
      <text x="333" y="359" font-size="8">2895.00</text>
      <text x="273" y="412" font-size="8">850.00</text>
    </g>
    <g font-family="Ubuntu, sans-serif" fill="#ffffff" text-anchor="middle" font-size="3.6">
      <text x="273" y="87">TQX-350</text>
      <text x="212" y="140">TQX-450</text>
      <text x="333" y="140">TVB-600</text>
      <text x="273" y="291">FREE DELIVERY &amp;</text>
      <text x="273" y="296">INSTALLATION</text>
      <text x="273" y="302">Dalvoss Exam Lane</text>
      <text x="212" y="365">DRA 4400</text>
      <text x="333" y="365">MEV PRT-3LED</text>
      <text x="273" y="418">MEV 24"</text>
    </g>
  </svg>

  <address class="address" style="font-style:normal">
    <svg class="abs" style="left:0;top:-26px" width="18" height="20" viewBox="0 0 18 20" aria-hidden="true"><path d="M9 1a6 6 0 0 0-6 6c0 4.5 6 11 6 11s6-6.5 6-11a6 6 0 0 0-6-6zm0 8.3a2.3 2.3 0 1 1 0-4.6 2.3 2.3 0 0 1 0 4.6z" fill="#5cb4ea"/></svg>
    Lakeside Optic Services<br>4820 Elm Ridge Rd.<br>Maple Falls, IL 60099
  </address>

  <div class="sell-tab">WE SELL NEW</div>
  <ul class="sell-list">
    <li>Chairs and Stands<svg class="chev" viewBox="0 0 12 12"><circle cx="6" cy="6" r="5.2" fill="none" stroke="#1f4f9a" stroke-width="1.2"/><path d="M7 3.5 4.5 6 7 8.5" fill="none" stroke="#1f4f9a" stroke-width="1.3"/></svg></li>
    <li>Sit Lamps<svg class="chev" viewBox="0 0 12 12"><circle cx="6" cy="6" r="5.2" fill="none" stroke="#1f4f9a" stroke-width="1.2"/><path d="M7 3.5 4.5 6 7 8.5" fill="none" stroke="#1f4f9a" stroke-width="1.3"/></svg></li>
    <li>Refractors<svg class="chev" viewBox="0 0 12 12"><circle cx="6" cy="6" r="5.2" fill="none" stroke="#1f4f9a" stroke-width="1.2"/><path d="M7 3.5 4.5 6 7 8.5" fill="none" stroke="#1f4f9a" stroke-width="1.3"/></svg></li>
    <li>Autolensometers<svg class="chev" viewBox="0 0 12 12"><circle cx="6" cy="6" r="5.2" fill="none" stroke="#1f4f9a" stroke-width="1.2"/><path d="M7 3.5 4.5 6 7 8.5" fill="none" stroke="#1f4f9a" stroke-width="1.3"/></svg></li>
    <li>Perimeters<svg class="chev" viewBox="0 0 12 12"><circle cx="6" cy="6" r="5.2" fill="none" stroke="#1f4f9a" stroke-width="1.2"/><path d="M7 3.5 4.5 6 7 8.5" fill="none" stroke="#1f4f9a" stroke-width="1.3"/></svg></li>
    <li>Autofractor/Keratometer<svg class="chev" viewBox="0 0 12 12"><circle cx="6" cy="6" r="5.2" fill="none" stroke="#1f4f9a" stroke-width="1.2"/><path d="M7 3.5 4.5 6 7 8.5" fill="none" stroke="#1f4f9a" stroke-width="1.3"/></svg></li>
    <li>Retinal Cameras and more<svg class="chev" viewBox="0 0 12 12"><circle cx="6" cy="6" r="5.2" fill="none" stroke="#1f4f9a" stroke-width="1.2"/><path d="M7 3.5 4.5 6 7 8.5" fill="none" stroke="#1f4f9a" stroke-width="1.3"/></svg></li>
  </ul>

  <ul class="contact-front">
    <li>312-555-0148<svg class="ico" viewBox="0 0 18 18"><circle cx="9" cy="9" r="8.5" fill="#2a5fb8"/><path d="M6.3 4.5c.5 0 1.5 2 1.3 2.5l-.8.8c.5 1.4 1.6 2.6 3 3.2l.8-.8c.5-.2 2.5.8 2.5 1.3 0 .9-1.2 2-2.1 1.9C8 13.1 4.9 10 4.6 7c-.1-1 1-2.5 1.7-2.5z" fill="#fff"/></svg></li>
    <li>lakesideeye@mailbox.com<svg class="ico" viewBox="0 0 18 18"><circle cx="9" cy="9" r="8.5" fill="#2a5fb8"/><rect x="4.5" y="6" width="9" height="6.5" rx="1" fill="#fff"/><path d="M4.8 6.4 9 9.6l4.2-3.2" fill="none" stroke="#2a5fb8" stroke-width="1"/></svg></li>
    <li>www.lakesideopticsvc.com<svg class="ico" viewBox="0 0 18 18"><circle cx="9" cy="9" r="8.5" fill="#2a5fb8"/><g fill="none" stroke="#fff" stroke-width=".9"><circle cx="9" cy="9" r="5"/><ellipse cx="9" cy="9" rx="2.2" ry="5"/><path d="M4 9h10M5 6.5h8M5 11.5h8"/></g></svg></li>
  </ul>
</section>

<section class="card card--back" aria-label="Postcard back">
  <svg class="layer" viewBox="0 0 641 428" aria-hidden="true">
    <defs>
      <linearGradient id="blueBack" x1="0" y1="0" x2="1" y2="1">
        <stop offset="0" stop-color="#234896"/><stop offset="1" stop-color="#2e5cb4"/>
      </linearGradient>
      <linearGradient id="silver" x1="0" y1="0" x2="1" y2="0">
        <stop offset="0" stop-color="#c9ccd1"/><stop offset=".55" stop-color="#ffffff"/><stop offset="1" stop-color="#c2c6cc"/>
      </linearGradient>
    </defs>
    <polygon points="275,0 385,212 275,428 0,428 0,0" fill="#f3f4f6"/>
    <polygon points="0,97 326,97 384,212 366,248 0,248" fill="url(#blueBack)"/>
    <polygon points="0,248 366,248 316,346 0,346" fill="url(#silver)"/>
    <polygon points="0,348 315,348 275,428 0,428" fill="url(#blueBack)"/>
    <polygon points="0,97 200,97 188,126 0,126" fill="var(--sky)"/>
    <polyline points="275,0 385,212 275,428" fill="none" stroke="var(--sky-light)" stroke-width="7"/>
  </svg>

  <div class="brand brand--back"><span class="brand__dot"></span><span>LAKESIDE OPTIC<br>SERVICES</span></div>

  <h2 class="also-title">WE ALSO DO</h2>
  <p class="also-text">Equipment Repair, Preventive Maintenance, Practice Relocation and Set-up and In-Office Service Calls.</p>

  <h2 class="services-title">OUR SERVICES</h2>
  <ul class="services">
    <li>Full Service Department</li>
    <li>Repair and Maintenance</li>
    <li>In-Office Service Calls</li>
    <li>Chairs and Stands, Lane Maintenance<br>and Urgent Repairs</li>
  </ul>

  <div class="abs" role="img" aria-label="Photo: slit lamp on table base" style="left:214px;top:40px;width:116px;height:151px;border-radius:6px;background:linear-gradient(160deg,#e8eaee,#9aa1ab)"></div>
  <div class="abs" role="img" aria-label="Photo: disassembled refractor parts being cleaned" style="left:15px;top:252px;width:112px;height:90px;border-radius:4px;background:linear-gradient(135deg,#cfd2d6,#6e7277)"></div>

  <p class="promo-label">REFRACTOR CLEANING</p>
  <p class="promo-price">ONLY 295.00</p>

  <ul class="contact-back">
    <li><svg class="ico ico--sm" viewBox="0 0 18 18"><circle cx="9" cy="9" r="8.5" fill="#4fb6ea"/><path d="M6.3 4.5c.5 0 1.5 2 1.3 2.5l-.8.8c.5 1.4 1.6 2.6 3 3.2l.8-.8c.5-.2 2.5.8 2.5 1.3 0 .9-1.2 2-2.1 1.9C8 13.1 4.9 10 4.6 7c-.1-1 1-2.5 1.7-2.5z" fill="#fff"/></svg>312-555-0148</li>
    <li><svg class="ico ico--sm" viewBox="0 0 18 18"><circle cx="9" cy="9" r="8.5" fill="#4fb6ea"/><rect x="4.5" y="6" width="9" height="6.5" rx="1" fill="#fff"/><path d="M4.8 6.4 9 9.6l4.2-3.2" fill="none" stroke="#4fb6ea" stroke-width="1"/></svg>lakesideeye@mailbox.com</li>
    <li><svg class="ico ico--sm" viewBox="0 0 18 18"><circle cx="9" cy="9" r="8.5" fill="#4fb6ea"/><g fill="none" stroke="#fff" stroke-width=".9"><circle cx="9" cy="9" r="5"/><ellipse cx="9" cy="9" rx="2.2" ry="5"/><path d="M4 9h10M5 6.5h8M5 11.5h8"/></g></svg>www.lakesideopticsvc.com</li>
  </ul>
</section>

</body>
</html>
```